Business Card Design For Marketing Agnecy LVT

Need business card design for marketing agency.

Dorian Pell
President, CEO
1-555-304-2917
dorian@lumenvaletrewards.net
www.LumenValeTrewards.biz

Back Side:
Boost Sales Using Rewards, Incentives & Giveaways
Get A Free Sample Package

Target Market(s)

B2B

Industry/Entity Type

Marketing

Contact Information for Business Card

Dorian Pell
President, CEO
1-555-304-2917

Back Side:
Get A Free Sample Package

Please note that my current url is OLD DESIGN. I am working on new design and want the business card to match color themes at least on new site. Here is the demo link for new site so you can see the colors I use, etc.

http://pagekilnstudio.example/qx/dorian/lvt_final/index.html

Requirements
Must have
• Please note that my current url is OLD DESIGN. I am working on new design and want the business card to match color themes at least on new site. Here is the demo link for new site so you can see the colors I use, etc.

Nice to have

Should not have

```html
<!DOCTYPE html>
<html lang="en">
<head>
<meta charset="utf-8">
<title>LVT Business Card</title>
<link href="https://fonts.googleapis.com/css2?family=Didact+Gothic&display=swap" rel="stylesheet">
<style>
  :root {
    --backdrop: #1f1f21;
    --card-blue: #2b7cc2;
    --card-grey: #56585b;
    --ink-light: #f2f3f4;
    --ink-soft: #d9dbdd;
  }
  * { margin: 0; padding: 0; box-sizing: border-box; }
  html, body { width: 1200px; height: 1000px; overflow: hidden; }
  body {
    background: var(--backdrop);
    font-family: "Didact Gothic", "Century Gothic", sans-serif;
    position: relative;
  }
  .card {
    position: absolute;
    top: 140px;
    width: 400px;
    height: 700px;
    border-radius: 26px;
    overflow: hidden;
    background: var(--card-grey);
    box-shadow: 0 18px 40px rgba(0,0,0,.45);
  }
  .card--front { left: 150px; }
  .card--back { left: 650px; }
  .card__band {
    position: absolute; inset: 0;
    background: var(--card-blue);
  }
  .card--front .card__band { clip-path: polygon(0 0, 100% 0, 100% 34%, 0 58%); }
  .card--back .card__band { clip-path: polygon(0 0, 100% 0, 100% 30%, 0 56%); }

  .brand {
    position: absolute;
    left: 0; right: 0;
    text-align: center;
    color: var(--ink-light);
    letter-spacing: 4px;
    line-height: 1;
    font-size: 92px;
  }
  .card--front .brand { top: 100px; }
  .card--back .brand { top: 390px; color: var(--card-blue); }

  .contact {
    position: absolute; left: 0; right: 0; top: 410px;
    text-align: center; color: var(--ink-light);
  }
  .contact__name { font-size: 30px; letter-spacing: 1.5px; }
  .contact__role { font-size: 20px; color: var(--ink-soft); margin-top: 4px; }
  .contact__icons {
    display: flex; justify-content: center; align-items: center;
    gap: 10px; margin-top: 14px;
  }
  .contact__icons::before, .contact__icons::after {
    content: ""; width: 62px; height: 2px; background: var(--ink-light); margin: 0 8px;
  }
  .contact__lines { margin-top: 18px; font-size: 17px; line-height: 1.75; letter-spacing: .3px; }

  .pitch {
    position: absolute; left: 48px; top: 70px;
    color: var(--ink-light); font-size: 22px; line-height: 2;
  }
  .site {
    position: absolute; left: 0; right: 0; bottom: 70px;
    text-align: center; color: var(--ink-light); font-size: 18px; letter-spacing: .3px;
  }
</style>
</head>
<body>
  <section class="card card--front" aria-label="Card front">
    <div class="card__band"></div>
    <div class="brand">LVT</div>
    <div class="contact">
      <div class="contact__name">DORIAN PELL</div>
      <div class="contact__role">CEO</div>
      <div class="contact__icons">
        <svg width="26" height="26" viewBox="0 0 26 26" aria-label="Phone">
          <rect x="1" y="1" width="24" height="24" rx="6" fill="none" stroke="#f2f3f4" stroke-width="2"/>
          <rect x="9" y="6" width="8" height="14" rx="1.5" fill="#f2f3f4"/>
        </svg>
        <svg width="26" height="26" viewBox="0 0 26 26" aria-label="Email">
          <rect x="1" y="1" width="24" height="24" rx="6" fill="none" stroke="#f2f3f4" stroke-width="2"/>
          <rect x="6" y="8" width="14" height="10" fill="#f2f3f4"/>
          <path d="M6 8 L13 14 L20 8" fill="none" stroke="#56585b" stroke-width="1.5"/>
        </svg>
        <svg width="26" height="26" viewBox="0 0 26 26" aria-label="Website">
          <rect x="1" y="1" width="24" height="24" rx="6" fill="none" stroke="#f2f3f4" stroke-width="2"/>
          <circle cx="13" cy="13" r="7" fill="#f2f3f4"/>
          <path d="M6 13 H20 M13 6 V20" stroke="#56585b" stroke-width="1.2"/>
        </svg>
      </div>
      <div class="contact__lines">
        <div>1-555-304-2917</div>
        <div>dorian@lumenvaletrewards.net</div>
        <div>www.LumenValeTrewards.biz</div>
      </div>
    </div>
  </section>

  <section class="card card--back" aria-label="Card back">
    <div class="card__band"></div>
    <div class="pitch">
      <div>Boost Sales Using Rewards</div>
      <div>Incentives &amp; Giveaways</div>
      <div>Get A Free Sample Package</div>
    </div>
    <div class="brand">LVT</div>
    <div class="site">www.lumenvaletrewards.biz</div>
  </section>
</body>
</html>
```